Business card for consulting firm

We need a double-sided business card for consulting firm, VantorQ. The card should be professional but also creative and visually interesting.

Target Market(s)

Engineering and technology; transport industries; safety critical / heavy industry.

Contact Information for Business Card

See attached file with details.

Font styles to use
Sans Serif

```html
<!DOCTYPE html>
<html lang="en">
<head>
<meta charset="utf-8">
<title>VantorQ Business Card</title>
<link href="https://fonts.googleapis.com/css2?family=Lato:wght@400;700;900&display=swap" rel="stylesheet">
<style>
  :root {
    --page-bg: #e6e6e6;
    --front-bg: #505a62;
    --back-bg: #0b2a75;
    --accent: #29b8e8;
    --white: #ffffff;
    --pattern-front: rgba(255, 255, 255, 0.07);
    --pattern-back: rgba(120, 150, 220, 0.18);
  }
  * { box-sizing: border-box; margin: 0; padding: 0; }
  html, body {
    width: 1200px;
    height: 1000px;
    overflow: hidden;
    background: var(--page-bg);
    font-family: "Lato", Arial, sans-serif;
    color: var(--white);
  }
  .card {
    position: absolute;
    width: 700px;
    height: 420px;
    overflow: hidden;
  }
  .card--front { left: 64px; top: 83px; background: var(--front-bg); }
  .card--back { left: 390px; top: 523px; background: var(--back-bg); }

  .texture {
    position: absolute;
    border-radius: 50%;
  }
  .card--front .texture {
    left: -20px; top: -60px; width: 320px; height: 320px;
    background: radial-gradient(circle at 45% 45%, var(--pattern-front), rgba(255,255,255,0.02) 70%);
  }
  .card--back .texture {
    left: 440px; top: -55px; width: 320px; height: 320px;
    background: radial-gradient(circle at 50% 45%, var(--pattern-back), rgba(120,150,220,0.05) 70%);
  }

  .brand {
    position: absolute;
    display: inline-flex;
    flex-direction: column;
    align-items: flex-end;
  }
  .card--front .brand { right: 39px; top: 58px; }
  .card--back .brand { left: 50px; top: 305px; }
  .brand__name {
    font-weight: 700;
    font-size: 50px;
    letter-spacing: 1px;
    line-height: 1;
    color: var(--white);
  }
  .brand__tagline {
    font-weight: 400;
    font-size: 17px;
    letter-spacing: 0.3px;
    margin-top: 6px;
  }

  .contact {
    position: absolute;
    left: 42px;
    top: 303px;
    list-style: none;
  }
  .contact__item {
    display: flex;
    align-items: center;
    height: 21px;
    font-weight: 700;
    font-size: 15px;
  }
  .contact__icon {
    width: 13px; height: 13px;
    margin-right: 8px;
    flex: none;
  }
  .contact__item--plain { padding-left: 21px; }

  .person {
    position: absolute;
    right: 39px;
    top: 333px;
    text-align: right;
  }
  .person__name {
    color: var(--accent);
    font-size: 17px;
    font-weight: 400;
    letter-spacing: 0.2px;
  }
  .person__credentials { font-size: 11px; margin-top: 2px; }
  .person__role { font-size: 12.5px; font-weight: 700; margin-top: 4px; }

  .accent-bar {
    position: absolute;
    right: 0; top: 335px;
    width: 28px; height: 50px;
    background: var(--accent);
  }
</style>
</head>
<body>

<section class="card card--front">
  <div class="texture" role="img" aria-label="Soft decorative bubble pattern texture"></div>

  <div class="brand">
    <span class="brand__name">VANTORQ</span>
    <span class="brand__tagline">Safety &amp; Human Factors</span>
  </div>

  <ul class="contact">
    <li class="contact__item">
      <svg class="contact__icon" viewBox="0 0 16 16"><path fill="#29b8e8" d="M3.5 1l2.5 3-1.5 2c.8 2 2.5 3.7 4.5 4.5l2-1.5 3 2.5-1.5 2.5C7 14 2 9 1 2.5z"/></svg>
      +61 (0)400 555 018
    </li>
    <li class="contact__item">
      <svg class="contact__icon" viewBox="0 0 16 16"><rect x="1" y="3" width="14" height="10" rx="1" fill="none" stroke="#29b8e8" stroke-width="1.6"/><path d="M1.5 4l6.5 5 6.5-5" fill="none" stroke="#29b8e8" stroke-width="1.6"/></svg>
      hbrightwater@vantorq.com.au
    </li>
    <li class="contact__item">
      <svg class="contact__icon" viewBox="0 0 16 16"><g fill="none" stroke="#29b8e8" stroke-width="1.3"><circle cx="8" cy="8" r="6.5"/><ellipse cx="8" cy="8" rx="3" ry="6.5"/><path d="M1.5 8h13M2.5 4.8h11M2.5 11.2h11"/></g></svg>
      www.vantorq.global
    </li>
    <li class="contact__item contact__item--plain">www.vantorq.com.au</li>
  </ul>

  <div class="person">
    <p class="person__name">HELENA BRIGHTWATER</p>
    <p class="person__credentials">BA (Hons), M Psych Org, M Tech Mgt (HF)</p>
    <p class="person__role">Managing Director</p>
  </div>
  <div class="accent-bar"></div>
</section>

<section class="card card--back">
  <div class="texture" role="img" aria-label="Soft decorative bubble pattern texture"></div>
  <div class="brand">
    <span class="brand__name">VANTORQ</span>
    <span class="brand__tagline">Safety &amp; Human Factors</span>
  </div>
</section>

</body>
</html>
```